Innovative Freezer Label Design

Create a versatile and innovative freezer label design with universal appeal, suitable for different functionalities. The design should cater to a diverse audience, including those who freeze meals for meal prepping, batch cooking, and the restaurant industry. Our vision is a visually striking and distinctive design that embodies simplicity.

Example "our current labels feature essential details like "Contents" and "Date." We recognize these as crucial points of information. Currently, the challenge lies in creating various labels for different marketplaces, considering language barriers. A proposed solution involves the integration of universal icons to replace specific words, promoting practicality for international sales."

Kindly note that design concepts should not be restricted to our current product, brand guideline, logo, or the provided example.

Our goal is not only product differentiation but also increased sales through a blend of functionality and aesthetics.

The following are examples of freezer labels designs. Kindly do not restrict your designs to the examples. The designs must be universal (for language barrier purposes)

Examples:
https://www.snaprovel.co.uk/pin/5820174630298837415/
https://www.snaprovel.co.uk/pin/5820174630298837419/
https://www.snaprovel.co.uk/pin/5820174630298837408/
https://www.snaprovel.co.uk/pin/5820174630298837322/
https://www.snaprovel.co.uk/pin/5820174630298898764/

Please reach out if you have any questions.

Thank you

```html
<!DOCTYPE html>
<html lang="en">
<head>
<meta charset="utf-8">
<title>KVL Freezer Label</title>
<link rel="stylesheet" href="https://fonts.googleapis.com/css2?family=Tinos:wght@400;700&display=swap">
<style>
  :root {
    --backdrop: #b1b1b1;
    --forest: #022526;
    --maroon: #4a1d18;
    --paper: #ffffff;
  }
  * { margin: 0; padding: 0; box-sizing: border-box; }
  html, body {
    width: 1200px;
    height: 851px;
    overflow: hidden;
    background: var(--backdrop);
    font-family: "Tinos", "Times New Roman", serif;
  }
  .canvas { position: relative; width: 1200px; height: 851px; }
  .label {
    position: absolute;
    left: 107px;
    top: 178px;
    width: 986px;
    height: 495px;
    border: 5px solid var(--maroon);
    border-radius: 26px;
    background: var(--paper);
    overflow: hidden;
  }
  .label__header {
    position: absolute;
    left: 0; top: 0;
    width: 100%;
    height: 224px;
    background: var(--forest);
    color: var(--paper);
    text-align: center;
  }
  .brand-name {
    position: absolute;
    left: 0; right: 0;
    top: 31px;
    font-size: 142px;
    font-weight: 700;
    line-height: 1;
    letter-spacing: 2px;
  }
  .brand-tagline {
    position: absolute;
    left: 0; right: 0;
    top: 156px;
    font-size: 48px;
    font-weight: 400;
    line-height: 1;
    letter-spacing: 3px;
  }
  .field {
    position: absolute;
    left: 0;
    display: flex;
    align-items: center;
    height: 51px;
    color: var(--maroon);
  }
  .field--contents { top: 249px; }
  .field--date { top: 378px; }
  .field__tab {
    width: 111px;
    height: 51px;
    background: var(--maroon);
    display: flex;
    align-items: center;
    justify-content: flex-end;
    padding-right: 6px;
  }
  .field__name {
    margin-left: 21px;
    font-size: 59px;
    font-weight: 700;
    line-height: 1;
  }
  .date-slash {
    position: absolute;
    top: 388px;
  }
</style>
</head>
<body>
<div class="canvas">
  <div class="label">
    <header class="label__header">
      <div class="brand-name">KVL</div>
      <div class="brand-tagline">Eco Friendly</div>
    </header>

    <div class="field field--contents">
      <div class="field__tab">
        <svg width="48" height="26" viewBox="0 0 48 26" aria-label="List icon" role="img">
          <g fill="var(--paper)">
            <circle cx="2.5" cy="3" r="2.3"/>
            <circle cx="2.5" cy="13" r="2.3"/>
            <circle cx="2.5" cy="23" r="2.3"/>
            <rect x="8" y="1" width="38" height="4.2"/>
            <rect x="8" y="11" width="38" height="4.2"/>
            <rect x="8" y="21" width="38" height="4.2"/>
          </g>
        </svg>
      </div>
      <span class="field__name">Contents:</span>
    </div>

    <div class="field field--date">
      <div class="field__tab">
        <svg width="38" height="40" viewBox="0 0 38 40" aria-label="Calendar icon" role="img">
          <g fill="none" stroke="var(--paper)" stroke-width="1.6">
            <rect x="1" y="5" width="36" height="34" rx="2.5"/>
            <rect x="3.5" y="11" width="31" height="25.5" rx="1"/>
          </g>
          <g fill="var(--paper)">
            <rect x="5.5" y="0.5" width="2.6" height="7" rx="1.2"/>
            <rect x="12.5" y="0.5" width="2.6" height="7" rx="1.2"/>
            <rect x="19.5" y="0.5" width="2.6" height="7" rx="1.2"/>
            <rect x="26.5" y="0.5" width="2.6" height="7" rx="1.2"/>
            <rect x="33" y="0.5" width="2.6" height="7" rx="1.2"/>
            <rect x="6" y="14" width="4" height="3.5"/><rect x="13" y="14" width="4" height="3.5"/><rect x="20" y="14" width="4" height="3.5"/><rect x="27" y="14" width="4" height="3.5"/>
            <rect x="6" y="20" width="4" height="3.5"/><rect x="13" y="20" width="4" height="3.5"/><rect x="20" y="20" width="4" height="3.5"/><rect x="27" y="20" width="4" height="3.5"/>
            <rect x="6" y="26" width="4" height="3.5"/><rect x="13" y="26" width="4" height="3.5"/><rect x="20" y="26" width="4" height="3.5"/><rect x="27" y="26" width="4" height="3.5"/>
          </g>
        </svg>
      </div>
      <span class="field__name">Date:</span>
    </div>

    <svg class="date-slash" style="left:338px" width="18" height="44" viewBox="0 0 18 44" aria-hidden="true">
      <polygon points="12,0 17,0 5,44 0,44" fill="var(--maroon)"/>
    </svg>
    <svg class="date-slash" style="left:453px" width="18" height="44" viewBox="0 0 18 44" aria-hidden="true">
      <polygon points="12,0 17,0 5,44 0,44" fill="var(--maroon)"/>
    </svg>
  </div>
</div>
</body>
</html>
```